Salve Label

2.25 inch round label.

We are looking for a simple label, muted natural colors, sophisticated, elegant, calming.

Name of Product: Herbal Beeswax Salve
This scent is lavender - but there will be others scents
Want this label to be adaptable to other scents with simple color and word changes.

Other things to express on the label - all natural, calming, relaxing

Name of the Company: Copper Hollow Farm
2 oz.

```html
<!DOCTYPE html>
<html lang="en">
<head>
<meta charset="UTF-8">
<title>Herbal Beeswax Salve – Lavender Label</title>
<link rel="stylesheet" href="https://fonts.googleapis.com/css2?family=Alegreya+SC:wght@400;500&family=Alegreya:wght@400&family=Pinyon+Script&display=swap">
<style>
  :root {
    --backdrop: #f3f2f4;
    --label-white: #ffffff;
    --scent-purple: #5b2b91;
    --scent-purple-deep: #4d2380;
    --sprig-tint: #b9a6d6;
    --ink: #231b26;
    --reverse-ink: #ffffff;
  }
  html, body {
    margin: 0;
    padding: 0;
    width: 1200px;
    height: 1200px;
    overflow: hidden;
    background: var(--backdrop);
  }
  .label {
    display: block;
    width: 1200px;
    height: 1200px;
  }
  .label-base { fill: var(--label-white); }
  .label-edge { fill: none; stroke: var(--ink); stroke-width: 4; }
  .label-inner-edge { fill: none; stroke: var(--ink); stroke-width: 2; }
  .scent-band { fill: var(--scent-purple); }
  .footer-band { fill: var(--label-white); }
  .scent-medallion { fill: var(--scent-purple-deep); stroke: var(--ink); stroke-width: 7; }
  .sprig-art { fill: var(--sprig-tint); opacity: 0.45; }
  .product-line {
    font-family: "Alegreya SC", "Alegreya", serif;
    font-size: 66px;
    letter-spacing: 13px;
    fill: var(--ink);
  }
  .farm-name {
    font-family: "Alegreya SC", "Alegreya", serif;
    font-size: 52px;
    letter-spacing: 2px;
    fill: var(--ink);
  }
  .scent-name {
    font-family: "Pinyon Script", cursive;
    font-size: 160px;
    fill: var(--reverse-ink);
  }
  .net-weight {
    font-family: "Alegreya", serif;
    font-size: 30px;
    letter-spacing: 1px;
    fill: var(--reverse-ink);
  }
</style>
</head>
<body>
<svg class="label" viewBox="0 0 1200 1200" xmlns="http://www.w3.org/2000/svg">
  <defs>
    <clipPath id="label-face">
      <circle cx="600" cy="600" r="520"/>
    </clipPath>
    <path id="top-arc" d="M 150,600 A 450 450 0 0 1 1050,600"/>
  </defs>

  <circle class="label-base" cx="600" cy="600" r="540"/>

  <g clip-path="url(#label-face)">
    <rect class="scent-band" x="0" y="548" width="1200" height="392"/>
    <rect class="footer-band" x="0" y="940" width="1200" height="260"/>

    <g class="sprig-left" role="img" aria-label="Line illustration of a lavender sprig">
      <rect class="sprig-art" x="162" y="570" width="52" height="290" rx="26"/>
    </g>
    <g class="sprig-right" role="img" aria-label="Line illustration of a lavender sprig">
      <rect class="sprig-art" x="986" y="570" width="52" height="290" rx="26"/>
    </g>
  </g>

  <g class="scent-medallion-group" role="img" aria-label="Scent medallion with faint botanical pattern">
    <circle class="scent-medallion" cx="600" cy="590" r="360"/>
  </g>

  <circle class="label-inner-edge" cx="600" cy="600" r="520"/>
  <circle class="label-edge" cx="600" cy="600" r="540"/>

  <text class="product-line">
    <textPath href="#top-arc" startOffset="50%" text-anchor="middle">HERBAL BEESWAX SALVE</textPath>
  </text>

  <text class="scent-name" x="600" y="630" text-anchor="middle">Lavender</text>
  <text class="net-weight" x="600" y="702" text-anchor="middle">NET WT: 2 OZ</text>

  <text class="farm-name" x="600" y="1010" text-anchor="middle" textLength="570" lengthAdjust="spacingAndGlyphs">COPPER HOLLOW FARM</text>
</svg>
</body>
</html>
```